Flyer für Computer Service
Zielgruppe
Privathaushalte und kleinere Firmen.
Wir möchten damit neue Kunden für unsere Dienstleistungen gewinnen.
Aufgabenstellung
Wir möchten mit diesem Flyer speziell unsere Computer Service Dienstleistungen bewerben.
Im wesentlichen werden folgende 3 Kategorieren von Dienstleistungen angeboten:
- Fernwartung
- Reparaturen
- Neuinstallationen, Backups und Virenentfernung
Fernwartung und Reparaturen bieten wir zu "ab EUR xx.-" Preisen an und Neuinstallationen, Backups und Virenentfernung zu Pauschalen.

```html
<!DOCTYPE html>
<html lang="de">
<head>
<meta charset="utf-8">
<title>relvano Computer Service</title>
<link href="https://fonts.googleapis.com/css2?family=Open+Sans:wght@600;700;800&display=swap" rel="stylesheet">
<style>
  :root{
    --orange:#f7941d;
    --orange-dark:#e2760c;
    --orange-light:#fbb45a;
    --blue:#2f80d2;
    --blue-deep:#1a5fae;
    --blue-sky:#8ec6ef;
    --blue-pale:#d6e8f6;
    --navy:#174d8c;
    --white:#ffffff;
  }
  *{margin:0;padding:0;box-sizing:border-box}
  html,body{width:849px;height:1200px;overflow:hidden;background:var(--white)}
  body{font-family:"Open Sans",Arial,sans-serif}
  .flyer{position:relative;width:849px;height:1200px;overflow:hidden;
    background:linear-gradient(180deg,var(--blue-sky) 0,#a9d3f2 55px,var(--white) 55px,var(--white) 60px,var(--orange) 60px)}
  .sunburst{position:absolute;left:0;top:60px;width:849px;height:330px;
    background:radial-gradient(ellipse at 58% 55%,var(--orange-light) 0%,var(--orange) 45%,var(--orange-dark) 100%)}
  .main-band{position:absolute;left:0;top:390px;width:849px;height:545px;
    background:linear-gradient(180deg,#5aa7e6 0%,var(--blue) 45%,#6fb1e6 85%,var(--blue-pale) 100%)}
  .foot-band{position:absolute;left:0;top:935px;width:849px;height:265px;
    background:linear-gradient(180deg,var(--blue-pale),#eef5fb 60%,var(--white))}

  .headline{position:absolute;left:45px;top:72px;color:var(--white);font-weight:800;font-size:33px;letter-spacing:.5px}
  .subline{position:absolute;left:45px;top:120px;color:var(--white);font-weight:700;font-size:22px}
  .subline .accent{color:var(--blue-deep)}
  .claim{position:absolute;left:45px;top:150px;color:var(--white);font-weight:700;font-size:21px}

  .portrait{position:absolute;left:321px;top:200px;width:348px;height:348px;border-radius:50%;
    border:7px solid var(--white);background:radial-gradient(circle at 50% 40%,#6fb3ea,var(--blue-deep));
    box-shadow:0 4px 14px rgba(0,0,0,.25)}
  .hardware{position:absolute;left:540px;top:492px;width:272px;height:185px;border-radius:6px;
    background:linear-gradient(135deg,#3b4654,#10161e 60%,#2a5c8c)}

  .features{position:absolute;left:306px;top:576px;list-style:none;color:var(--white);font-weight:700;font-size:16px;line-height:19.5px}
  .features li{position:relative;padding-left:20px}
  .features li::before{content:"";position:absolute;left:0;top:6px;width:8px;height:8px;background:var(--orange);border:1px solid var(--white)}

  .hotline{position:absolute;left:307px;top:686px;color:var(--orange);font-weight:800;font-size:23px;letter-spacing:.5px}
  .brand{position:absolute;left:300px;top:700px;width:512px;text-align:center;color:var(--orange);font-weight:800;font-size:128px;letter-spacing:-2px;line-height:150px}
  .web{position:absolute;right:47px;top:842px;color:var(--blue-deep);font-weight:800;font-size:21px}
  .web .hi{color:var(--orange)}
  .address{position:absolute;left:310px;top:876px;color:var(--navy);font-weight:700;font-size:18.5px}

  .service{position:absolute;width:224px;height:214px;border:4px solid var(--orange);
    background:linear-gradient(180deg,#4e9be0,var(--blue-deep));color:var(--white);box-shadow:0 2px 6px rgba(0,0,0,.2)}
  .service-title{height:36px;background:linear-gradient(180deg,#8ec6ef,#4f9be0);color:var(--orange);font-weight:800;font-size:20px;
    text-align:center;line-height:36px;letter-spacing:.3px;text-shadow:0 0 2px var(--white),0 0 2px var(--white)}
  .service-text{padding:8px 12px 0;font-size:11.5px;font-weight:700;line-height:15.5px}
  .price{position:absolute;left:0;right:0;bottom:10px;text-align:center;font-weight:800;font-size:19px}
  .price .amount{color:var(--orange);font-size:30px;vertical-align:-3px;margin-left:4px}
  .price-pill{display:inline-block;padding:0 14px;border-radius:20px;background:rgba(20,70,130,.45)}

  .s-rep{left:42px;top:442px}
  .s-fern{left:42px;top:693px}
  .s-neu{left:42px;top:948px}
  .s-back{left:307px;top:948px}
  .s-viren{left:586px;top:948px}
</style>
</head>
<body>
<main class="flyer">
  <div class="sunburst" role="img" aria-label="Orangefarbener Strahlenhintergrund"></div>
  <div class="main-band"></div>
  <div class="foot-band"></div>

  <h1 class="headline">BRAUCHEN SIE HILFE MIT IHREM PC ???</h1>
  <p class="subline">...kein Problem, <span class="accent">wir helfen Ihnen Sofort</span></p>
  <p class="claim">Professinal, Schnell und Günstig</p>

  <div class="portrait" role="img" aria-label="Foto eines Technikers im Anzug mit Laptop"></div>
  <div class="hardware" role="img" aria-label="Illustration von Laptop, Desktop-PC, Tastatur und Maus"></div>

  <ul class="features">
    <li>Schneller Service</li>
    <li>Fixe Tiefpreise</li>
    <li>Kompetente Beratung</li>
    <li>Professioneller Support</li>
  </ul>

  <p class="hotline">Infos unter : 0800 / 5550190</p>
  <p class="brand">relvano</p>
  <p class="web">www.<span class="hi">relvano</span>.ch</p>
  <p class="address">Relvano GmbH - Musterstr.12 - Musterhausen 33667</p>

  <section class="service s-rep">
    <h2 class="service-title">REPERATUREN</h2>
    <p class="service-text">Hier könnte ihr Feintext stehen der Ihre Leistung genau erklährt. Hier könnte ihr Feintext stehen der Ihre Leistung genau erklährt. Hier könnte ihr Feintext stehen der Ihre Leistung genau erklährt. Hier könnte ihr Feintext</p>
    <p class="price"><span class="price-pill">schon ab<span class="amount">59 €</span></span></p>
  </section>

  <section class="service s-fern">
    <h2 class="service-title">FERNWARTUNG</h2>
    <p class="service-text">Hier könnte ihr Feintext stehen der Ihre Leistung genau erklährt. Hier könnte ihr Feintext stehen der Ihre Leistung genau erklährt. Hier könnte ihr Feintext stehen der Ihre Leistung genau erklährt. Hier könnte ihr Feintext</p>
    <p class="price"><span class="price-pill">schon ab<span class="amount">49 €</span></span></p>
  </section>

  <section class="service s-neu">
    <h2 class="service-title">NEUINSTALATION</h2>
    <p class="service-text">Hier könnte ihr Feintext stehen der Ihre Leistung genau erklährt. Hier könnte ihr Feintext stehen der Ihre Leistung genau erklährt. Hier könnte ihr Feintext stehen der Ihre Leistung genau erklährt. Hier könnte ihr Feintext</p>
    <p class="price"><span class="price-pill">nur<span class="amount">29 €</span></span></p>
  </section>

  <section class="service s-back">
    <h2 class="service-title">BACKUPS</h2>
    <p class="service-text">Hier könnte ihr Feintext stehen der Ihre Leistung genau erklährt. Hier könnte ihr Feintext stehen der Ihre Leistung genau erklährt. Hier könnte ihr Feintext stehen der Ihre Leistung genau erklährt. Hier könnte ihr Feintext</p>
    <p class="price"><span class="price-pill">nur<span class="amount">39 €</span></span></p>
  </section>

  <section class="service s-viren">
    <h2 class="service-title">VIRENENTFERNUNG</h2>
    <p class="service-text">Hier könnte ihr Feintext stehen der Ihre Leistung genau erklährt. Hier könnte ihr Feintext stehen der Ihre Leistung genau erklährt. Hier könnte ihr Feintext stehen der Ihre Leistung genau erklährt. Hier könnte ihr Feintext</p>
    <p class="price"><span class="price-pill">nur<span class="amount">49 €</span></span></p>
  </section>
</main>
</body>
</html>
```